Crate Up! Flyer Design - Double Sided, Get Creative!

We are looking for a flexible flyer design, DL sized print.

We are launching a new service - Crate Up! - which is basically a personal, urban self storage solution. We deliver boxes, our customer pack them, we collect and store and can re-deliver on demand.

For colour, logo and a better idea of the service please see our website www.simplycrateup.com.au

One side of the flyer will need a picture of the box, explanation of the service, a call to action with an offer, as well as a price. The tag line is Simply Crate UP!

The other side is where we need creative input. We are looking for something clean and modern, that appeals to a market 18 - 45. I am happy to explore the idea of multiple different concepts to target each market (ie. one targeting mothers, one targeting students, etc) and will pay for each of those if the concept is good.

Our target market is apartment dwellers, students, mothers with young children (but who have outgrown toys, etc), older people whose kids have left home, and people moving to smaller houses from larger ones.

The value proposition of our service is that:

1, Very cost effective
2 .Very convenient (delivered to/from your door)
3. No wasted space, so not wasting money

Please take inspiration from our website for font and colours.

Hi All,Just wanted to add that we are also going to need other collateral once this is done - posters, etc. So please think of this as more than just a one off job! Added Tuesday, February 24, 2015

Target Market(s)

People looking for storage of items / stuff. Our target market is apartment dwellers, students, mothers with young children (but who have outgrown toys, etc), older people whose kids have left home, and people moving to smaller houses from larger ones.

Industry/Entity Type

Self Storage

Font styles to use
Sans Serif

Requirements
Must have
• Our logo, a picture of our box, our value propositions, how the service works, call to action / offer.
• Side 1: Communicate the Idea of storage, mess - tidy. Maybe a cover to target each market vertical.
• Side 2: Picture of our box, our value propositions, how the service works, call to action / offer.
Nice to have
• Idea of mess -> tidy, etc.

```html
<!DOCTYPE html>
<html lang="en">
<head>
<meta charset="utf-8">
<title>Crate Up! – Flyer</title>
<link rel="stylesheet" href="https://fonts.googleapis.com/css2?family=Open+Sans:ital,wght@0,400;0,600;0,700;0,800;1,600;1,700&family=Oswald:wght@600&family=PT+Serif&family=Dancing+Script:wght@700&display=swap">
<style>
:root{
  --stage:#2b2b2b;
  --brand-blue:#1e9ad6;
  --sky:#8fd3f2;
  --sky-pale:#e6f6fd;
  --teal-dark:#1f5d78;
  --navy:#0f2f47;
  --band-blue:#2a9fd8;
  --orange:#f7a21b;
  --ink:#1a1a1a;
  --white:#ffffff;
  --grass:#c9e6a3;
}
*{box-sizing:border-box;margin:0;padding:0}
html,body{width:1200px;height:1139px;overflow:hidden;background:var(--stage);font-family:"Open Sans",Arial,sans-serif}
.flyer{position:absolute;overflow:hidden}

/* ---------- front ---------- */
.front{left:58px;top:50px;width:1084px;height:512px;
  background:linear-gradient(180deg,#5fc3ee 0%,#bfe7f8 35%,#e9f7fb 60%,var(--grass) 100%)}
.wordmark{position:absolute;display:flex;align-items:center;gap:12px;color:var(--brand-blue);font-weight:800;font-size:60px;line-height:1;letter-spacing:-1px;white-space:nowrap}
.wordmark .mark{width:40px;height:40px;background:var(--brand-blue)}
.front .wordmark{left:36px;top:26px}
.tagline{position:absolute;left:36px;top:104px;font-style:italic;font-weight:700;font-size:22px;color:var(--ink)}
.offer-panel{position:absolute;left:17px;top:216px;width:298px;height:192px;border-radius:8px;
  background:linear-gradient(165deg,#bfeafb 0%,#4fb8e6 40%,#16496b 80%,var(--navy) 100%);box-shadow:0 2px 6px rgba(0,0,0,.35)}
.offer-seal{position:absolute;left:106px;top:144px;width:84px;height:84px;border-radius:50%;background:#1c1c1c;border:4px solid #555;
  display:flex;align-items:center;justify-content:center;color:var(--white);font-weight:800;font-size:17px}
.price-from{position:absolute;left:10px;top:10px;font-family:"Dancing Script",cursive;font-size:38px;color:var(--navy);transform:rotate(-8deg)}
.price{position:absolute;left:46px;top:22px;font-weight:800;font-size:64px;color:var(--white);transform:rotate(-6deg);text-shadow:0 2px 3px rgba(0,0,0,.4)}
.price-unit{position:absolute;right:16px;font-weight:800;font-size:30px;color:var(--ink);text-align:right;white-space:nowrap;
  -webkit-text-stroke:1px var(--white);text-shadow:0 0 2px var(--white)}
.price-unit.box{top:110px}
.price-unit.month{top:148px}
.hero-photo{position:absolute;left:350px;top:14px;width:330px;height:394px;border-radius:6px;
  background:radial-gradient(ellipse at 55% 70%,#2f7fd0 0%,#8cc4ea 45%,rgba(255,255,255,0) 75%)}
.services-splash{position:absolute;left:758px;top:10px;width:320px;height:150px;border-radius:50% 40% 45% 50%;
  background:radial-gradient(ellipse at 40% 55%,var(--orange) 0%,#f59a14 55%,rgba(247,162,27,0) 72%)}
.services-title{position:absolute;left:778px;top:66px;font-family:"Oswald",sans-serif;font-weight:600;font-size:40px;color:#222}
.services-list{position:absolute;left:689px;top:188px;width:380px;list-style:none;font-size:15.5px;line-height:19.5px;color:var(--ink)}
.services-list li{position:relative;padding-left:28px}
.services-list li::before{content:"";position:absolute;left:4px;top:5px;width:10px;height:10px;background:var(--brand-blue);transform:rotate(45deg)}
.front .stripe{position:absolute;left:0;top:415px;width:100%;height:22px;background:var(--band-blue)}
.front .contact-band{position:absolute;left:0;top:442px;width:100%;height:70px;background:var(--teal-dark);color:var(--white);display:flex;align-items:center;white-space:nowrap}
.front .contact-band .phone{font-weight:700;font-size:29px;padding-left:36px;width:358px}
.front .contact-band .divider{width:2px;height:42px;background:rgba(255,255,255,.6)}
.front .contact-band .email{font-size:15px;width:298px;text-align:center}
.front .contact-band .web{font-weight:700;font-size:24px;flex:1;text-align:center;letter-spacing:.5px;padding-right:10px}

/* ---------- back ---------- */
.back{left:54px;top:586px;width:1086px;height:512px;background:linear-gradient(180deg,#ffffff 0%,#e2f3fb 45%,#a9dcf3 80%)}
.steps-head{position:absolute;left:10px;top:37px;width:250px;height:41px;background:var(--teal-dark);color:var(--white);
  font-style:italic;font-weight:600;font-size:19px;display:flex;align-items:center;padding-left:14px;clip-path:polygon(0 0,100% 0,97% 100%,3% 100%)}
.step{position:absolute;left:10px;width:250px;height:70px;color:var(--white);text-align:center;padding-top:4px}
.step.light{background:var(--band-blue)}
.step.dark{background:var(--teal-dark)}
.step h3{font-weight:600;font-size:19px;line-height:24px}
.step p{font-size:13.5px;line-height:17px}
.shelf-photo{position:absolute;left:289px;top:20px;width:342px;height:344px;
  background:linear-gradient(180deg,#d8bb8c 0%,#c9a46e 60%,#b9b9b9 100%);opacity:.9}
.back .wordmark{left:723px;top:22px;font-size:56px}
.store-card{position:absolute;left:666px;top:140px;width:410px;height:276px;border:6px solid var(--white);border-radius:12px;
  background:linear-gradient(180deg,#5ec9f3 0%,#b6e5f8 40%,#eaf7fd 100%);transform:rotate(5deg);box-shadow:0 3px 8px rgba(0,0,0,.3);padding:24px 26px;z-index:2}
.store-card h2{font-style:italic;font-weight:700;font-size:28px;text-align:center;color:var(--ink);margin-bottom:10px}
.store-card p{font-family:"PT Serif",serif;font-size:17px;line-height:19px;text-align:justify;color:var(--ink)}
.back .stripe{position:absolute;left:0;top:384px;width:100%;height:22px;background:var(--teal-dark)}
.back .contact-band{position:absolute;left:0;top:414px;width:100%;height:98px;background:var(--band-blue);white-space:nowrap}
.back .phone{position:absolute;left:30px;top:16px;width:290px;text-align:center;font-weight:700;font-size:27px;color:var(--ink)}
.back .email{position:absolute;left:30px;top:58px;width:290px;text-align:center;font-size:14.5px;color:var(--ink)}
.back .address{position:absolute;left:439px;top:20px;font-size:17px;color:var(--ink)}
.back .web{position:absolute;left:439px;top:44px;font-weight:700;font-size:30px;color:var(--ink)}
</style>
</head>
<body>

<section class="flyer front">
  <div class="wordmark"><span class="mark"></span>Crate Up!</div>
  <p class="tagline">Safe, secure and insured storage</p>

  <div class="offer-panel">
    <span class="price-from">From</span>
    <span class="price">$5.95</span>
    <span class="price-unit box">PER BOX</span>
    <span class="price-unit month">PER MONTH</span>
  </div>
  <div class="offer-seal">OFFER</div>

  <div class="hero-photo" role="img" aria-label="Delivery man with a hand trolley of cardboard boxes and two blue storage crates filled with clothes"></div>

  <div class="services-splash" role="img" aria-label="Orange paint stroke with a paint roller"></div>
  <h2 class="services-title">Services:</h2>
  <ul class="services-list">
    <li>We deliver you empty boxes free of charge.</li>
    <li>You pack your boxes and apply our tamper seals</li>
    <li>We collect and securely store your boxes &amp; items, from $5.95 per month</li>
    <li>When you need something back, we deliver it to you within 24 hours</li>
    <li>Much more cost effective and convenient than self storage</li>
    <li>Manage your boxes online, record the contents with photos (COMING SOON)</li>
  </ul>

  <div class="stripe"></div>
  <div class="contact-band">
    <span class="phone">Ph: 1300-624-518</span>
    <span class="divider"></span>
    <span class="email">Email: hello@simplycrateup.com.au</span>
    <span class="divider"></span>
    <span class="web">www.simplycrateup.com.au</span>
  </div>
</section>

<section class="flyer back">
  <div class="steps-head">How the service works</div>
  <div class="step light" style="top:82px"><h3>We Deliver</h3><p>To your door, at your convenience<br>for FREE.</p></div>
  <div class="step dark" style="top:156px"><h3>You Pack</h3><p>Take your time, pack at your own<br>pace - we give you up to a week.</p></div>
  <div class="step light" style="top:230px"><h3>We Collect &amp; Store</h3><p>When you're ready we collect<br>your filled boxes, for FREE.</p></div>
  <div class="step dark" style="top:302px"><h3>We Return</h3><p>When you need something we<br>can drop it back within 24 hours</p></div>

  <div class="shelf-photo" role="img" aria-label="Woman in a business suit pulling a cardboard box from a metal shelving unit full of archive boxes"></div>

  <div class="wordmark"><span class="mark"></span>Crate Up!</div>

  <div class="stripe"></div>
  <div class="contact-band">
    <span class="phone">Ph: 1300-624-518</span>
    <span class="email">Email: hello@simplycrateup.com.au</span>
    <span class="address">PO BOX 482 Elmwood North 3170,Melbourne</span>
    <span class="web">www.simplycrateup.com.au</span>
  </div>

  <div class="store-card">
    <h2>What can I store?</h2>
    <p>There are lots of examples of what you might want to store in Crate Up boxes. These inlcuded books, clothing, documents, old toys, sentimental objects and the like. However you would want to avoid really fragile objects (glass, pottery etc). If in doubt give us a call, and always wrap it in bubble wrap</p>
  </div>
</section>

</body>
</html>
```